ebook cover: book 4 in the We Hum Lantern series. Lantern by Riverside

I am wanting a striking cover to bring the forth book in a spiritual journey series to an audience ready to meet new characters and get excited again! White backgrounds, red titles (any font), subtitles to introduce a new major character in the series of ten (same fonts please as the original, We Hum Lantern), and one emblematic, slightly mysterious image. Please keep to the same colour tones as the original, but the lead image need not be gray. Let's please try to use the "light flash" that is on the tin can in We Hum Lantern somehow, in your own way. It is meant to signify the other side, or the higher light, or some such inference.

Book details:
Title: Lantern by Riverside
Subtitle: Archangel Veloriel brings the message
Image: silver hourglass
Author: Maren Tulliver, Ph.D
Strap quote: "Tulliver is smart, savvy and full of ideas," Harbourgate Ledger

Please do your best: this one is going in competition of spiritual healers!

Thanks! :)

```html
<!DOCTYPE html>
<html lang="en">
<head>
<meta charset="utf-8">
<title>Lantern by Riverside — Ebook Cover</title>
<link rel="stylesheet" href="https://fonts.googleapis.com/css2?family=Arimo:ital@0;1&family=Libre+Baskerville&family=Montserrat:wght@300&family=Oswald:wght@700&display=swap">
<style>
  :root {
    --backdrop: #e0e0e0;
    --cover: #ffffff;
    --title-red: #ed1c24;
    --ink: #111111;
    --glass-light: #f2b9a4;
    --glass-mid: #c9826c;
    --frame-dark: #3a2420;
  }
  html, body {
    margin: 0;
    padding: 0;
    width: 1200px;
    height: 1200px;
    overflow: hidden;
    background: var(--backdrop);
  }
  .canvas { display: block; width: 1200px; height: 1200px; }
  .cover-sheet { fill: var(--cover); }
  .strap-quote { font-family: "Arimo", Arial, sans-serif; font-style: italic; font-size: 27px; fill: var(--ink); }
  .strap-source { font-family: "Arimo", Arial, sans-serif; font-size: 27px; fill: var(--ink); }
  .title-main { font-family: "Oswald", "Arial Narrow", sans-serif; font-weight: 700; font-size: 122px; fill: var(--title-red); }
  .title-joiner { font-family: "Libre Baskerville", "Times New Roman", serif; font-size: 72px; fill: var(--ink); }
  .subtitle { font-family: "Montserrat", Helvetica, sans-serif; font-weight: 300; font-size: 39px; fill: var(--ink); }
  .author { font-family: "Libre Baskerville", "Times New Roman", serif; font-size: 36px; fill: var(--ink); }
</style>
</head>
<body>
<svg class="canvas" viewBox="0 0 1200 1200" xmlns="http://www.w3.org/2000/svg">
  <defs>
    <linearGradient id="hourglass-tone" x1="0" y1="0" x2="0" y2="1">
      <stop offset="0" stop-color="var(--frame-dark)"/>
      <stop offset="0.15" stop-color="var(--glass-mid)"/>
      <stop offset="0.5" stop-color="var(--glass-light)"/>
      <stop offset="0.85" stop-color="var(--glass-mid)"/>
      <stop offset="1" stop-color="var(--frame-dark)"/>
    </linearGradient>
  </defs>

  <rect class="cover-sheet" x="255" y="82" width="692" height="1037"/>

  <g class="strap">
    <text class="strap-quote" x="601" y="134" text-anchor="middle">"Tulliver is smart, savvy and full of ideas,"</text>
    <text class="strap-source" x="601" y="175" text-anchor="middle">-Harbourgate Ledger-</text>
  </g>

  <g class="title">
    <text class="title-main" x="601" y="328" text-anchor="middle" textLength="454" lengthAdjust="spacingAndGlyphs">LANTERN</text>
    <text class="title-joiner" x="601" y="400" text-anchor="middle">BY</text>
    <text class="title-main" x="601" y="508" text-anchor="middle" textLength="546" lengthAdjust="spacingAndGlyphs">RIVERSIDE</text>
  </g>

  <g class="subtitle-block">
    <text class="subtitle" x="601" y="564" text-anchor="middle" textLength="454" lengthAdjust="spacingAndGlyphs">ARCHANGEL VELORIEL</text>
    <text class="subtitle" x="601" y="604" text-anchor="middle" textLength="446" lengthAdjust="spacingAndGlyphs">BRINGS THE MESSAGE</text>
  </g>

  <rect class="lead-image" x="484" y="628" width="236" height="388" rx="18" fill="url(#hourglass-tone)" role="img" aria-label="Ornate hourglass with dark carved frame and glowing rose-tinted glass"/>

  <text class="author" x="601" y="1082" text-anchor="middle" textLength="460" lengthAdjust="spacing">MAREN TULLIVER, PH.D</text>
</svg>
</body>
</html>
```